Pet Shop Website

website will need to have the following features:
• Photo Galleries of each species (Dogs, Cats, Birds, Fish, Reptiles, Rabbits) in a light box popup
o Each species may have several different categories for example:
 Fish
• Marine fish
• Fresh water
• tropical
• Cichlid
• Information Fact sheets of each species – Downloaded as a pdf which can be either
o Care Sheets
o Training Sheets
• Members Area
o Username (Email Address) & Password login
o New signups
o Exclusive Member Deals
o Newsletter options

The front page must be very simple (for example lumavale.com.au) contain the following:
• Product of the week - which can be purchased online
o Short details
o Cost
• Pet Club Sign up picture
• Animal of the week/month
• Contact Phone Number and addresses of the stores
• A jQuery slideshow (Images could include stores, pets etc…)
The main page MUST keep simple. We do not want it cluttered.

Inner Page
The animals / reptile page will need to have:
• Short description of the species
• Photo Galleries
• A list of what is in stock and the list needs to clearly be sorted by each store (Use of Tabs maybe).
• Facts sheets / Info sheets
The type of website ideas (not the type of look that we are necessary after) is and the sort of content that we want to offer are as follows:

http://www.scalenook.com.au/
http://www.marrowdenpets.com.au/
http://www.thefurloft.com.au
http://www.critterhaven.net.au

Colour in the new website:
Blue
Red
Grey
Yellow

Original site:

http://www.pawglint.com.au
Updates

Hi Guys,

We had feedback from the client and they would like to see a few dark designs.

Thanks                                   

Reason: We would like to reopen this contest back up for a further week

Target Market(s)

Targeting animal lovers

Industry/Entity Type

Store

Requirements
Should not have
• Alter the logo in anyway

```html
<!DOCTYPE html>
<html lang="en">
<head>
<meta charset="utf-8">
<title>Pawglint – Pet Superstores</title>
<link href="https://fonts.googleapis.com/css2?family=Baloo+2:wght@600;700;800&family=Arimo:wght@400;700&family=Roboto+Condensed:wght@400&family=Open+Sans:wght@600&display=swap" rel="stylesheet">
<style>
:root{
  --navy:#0d1478;
  --navy-dark:#070b52;
  --red:#e00010;
  --yellow:#f2d400;
  --grey:#5a5a5a;
  --grey-mid:#7b7b7b;
  --line:#cfcfcf;
  --paper:#f4f3ef;
  --white:#ffffff;
  --ink:#222;
}
*{margin:0;padding:0;box-sizing:border-box}
html,body{width:1200px;height:1150px;overflow:hidden}
body{background:var(--paper);font-family:"Arimo",Arial,sans-serif;color:var(--ink);position:relative}
.abs{position:absolute}
.ph{position:absolute}

/* header */
.header{left:0;top:0;width:1200px;height:118px;background:linear-gradient(#ffffff,#ececec)}
.header-band{left:0;top:116px;width:1200px;height:8px;background:linear-gradient(#c8c8c8,#ededed)}
.brand{left:132px;top:22px;display:flex;align-items:center;gap:12px}
.brand-mark{width:22px;height:22px;background:var(--yellow)}
.brand-name{font-family:"Baloo 2",sans-serif;font-weight:800;font-size:46px;color:var(--navy);line-height:1}
.call{right:121px;top:8px;font-family:"Baloo 2",sans-serif;font-weight:600;font-size:26px;color:var(--grey)}
.mascot{left:745px;top:30px;width:112px;height:95px;border-radius:40px 40px 6px 6px;background:radial-gradient(#f2e4cc,#c9a67a)}
.follow{left:993px;top:61px;font-family:"Baloo 2",sans-serif;font-weight:600;font-size:14px;color:#333}
.social{left:918px;top:83px;display:flex;gap:5px}
.social span{width:23px;height:23px;border-radius:3px;background:linear-gradient(#8a97b8,#4a5a85)}

/* nav */
.nav{left:110px;top:146px;width:979px;height:39px;background:linear-gradient(#1b24a0,var(--navy-dark));display:flex;align-items:center}
.fold{top:185px;width:0;height:0;border-top:12px solid var(--navy-dark)}
.fold.l{left:110px;border-left:14px solid transparent;transform:scaleX(-1)}
.fold.r{left:1075px;border-left:14px solid transparent}
.fold.l{border-left:none;border-right:14px solid transparent;transform:none}
.nav-item{font-family:"Open Sans",sans-serif;font-weight:600;font-size:13px;color:var(--white);text-align:center;position:absolute;top:10px}
.nav-item.active{left:15px;top:4px;width:102px;height:30px;line-height:30px;background:var(--yellow);color:var(--ink);border-radius:16px}
.nav-sep{position:absolute;top:7px;width:1px;height:25px;background:#3a44b0}
.search{position:absolute;left:743px;top:6px;width:215px;height:27px;border-radius:14px;background:var(--white);font-size:11px;color:#555;padding:6px 0 0 13px}
.search svg{position:absolute;right:9px;top:4px}

/* slider */
.slide-frame{left:130px;top:203px;width:941px;height:311px;background:var(--white);border:1px solid #ddd}
.slide-inner{left:137px;top:210px;width:929px;height:297px;background:linear-gradient(#e4e4e4,#ffffff)}
.slide-photo{left:140px;top:212px;width:380px;height:294px;background:linear-gradient(160deg,#e6e6e6,#b38a5a 55%,#6e4a2a)}
.slide-shadow{left:160px;top:514px;width:880px;height:22px;background:radial-gradient(ellipse at top,rgba(0,0,0,.18),transparent 70%)}
.welcome{left:514px;top:222px;font-family:"Baloo 2",sans-serif;font-weight:700;font-size:30px;color:var(--grey)}
.headline{left:512px;top:256px;font-family:"Baloo 2",sans-serif;font-weight:800;font-size:45px;color:var(--red);letter-spacing:.2px}
.subline{left:514px;top:302px;font-family:"Baloo 2",sans-serif;font-weight:700;font-size:27px;color:var(--yellow)}
.ticks{left:517px;top:356px;list-style:none;font-size:12px;color:#333}
.ticks li{height:22px;display:flex;align-items:center;gap:8px}
.readmore{left:918px;top:452px;width:129px;height:39px;border-radius:10px;background:linear-gradient(#2b35b0,var(--navy-dark));border:2px solid #a9add8;color:var(--white);font-family:"Baloo 2",sans-serif;font-weight:700;font-size:16px;display:flex;align-items:center;justify-content:center;gap:6px}
.slide-arrow{top:321px;width:47px;height:50px;background:var(--grey-mid);display:flex;align-items:center;justify-content:center}

/* features */
.feature-panel{left:133px;top:583px;width:931px;height:240px;background:linear-gradient(transparent 60%,var(--white));border-radius:0 0 8px 8px}
.panel-wing{top:780px;width:40px;height:40px;background:linear-gradient(transparent,#bdbdbd)}
.col-rule{top:584px;width:0;height:234px;border-left:1px dotted #aaa}
.col-title{top:582px;font-family:"Baloo 2",sans-serif;font-weight:700;font-size:21px;color:#333;letter-spacing:.5px}
.col-text{font-size:12px;line-height:18px;color:#333;width:262px;text-align:justify;letter-spacing:.4px}
.pager{left:1008px;top:797px}

/* portfolio */
.port-icon{left:135px;top:853px;width:60px;height:45px;border-radius:50%;background:radial-gradient(#ff8a2a,#e55b00)}
.port-title{left:201px;top:858px;font-family:"Baloo 2",sans-serif;font-weight:700;font-size:24px;color:var(--navy);letter-spacing:.6px}
.port-rule{left:190px;top:897px;width:830px;border-top:1px dotted #bbb}
.thumb{box-shadow:0 6px 8px -6px rgba(0,0,0,.35)}

/* footer */
.foot-rule{left:180px;top:1054px;width:830px;border-top:1px dotted #bbb}
.foot-links{left:135px;top:1077px;font-family:"Roboto Condensed",sans-serif;font-size:12px;color:#333;display:flex;gap:16px}
.copy{left:135px;top:1097px;font-family:"Roboto Condensed",sans-serif;font-size:12px;color:#333}
.address{right:130px;top:1076px;font-family:"Roboto Condensed",sans-serif;font-size:12px;line-height:16px;color:#333;text-align:right}
</style>
</head>
<body>

<header>
  <div class="abs header"></div>
  <div class="abs header-band"></div>
  <div class="abs brand"><span class="brand-mark"></span><span class="brand-name">Pawglint</span></div>
  <div class="abs call">Call : (08) 9410 2275</div>
  <div class="ph mascot" role="img" aria-label="Puppy peeking over the header edge"></div>
  <div class="abs follow">Follow Us on:</div>
  <div class="abs social"><span></span><span></span><span></span><span></span><span></span><span></span></div>
</header>

<nav class="abs nav">
  <span class="nav-item active">Home Page</span>
  <span class="nav-sep" style="left:135px"></span>
  <span class="nav-item" style="left:167px">About Us</span>
  <span class="nav-sep" style="left:260px"></span>
  <span class="nav-item" style="left:305px">Pets</span>
  <span class="nav-sep" style="left:363px"></span>
  <span class="nav-item" style="left:394px">Contact us</span>
  <span class="nav-sep" style="left:480px"></span>
  <div class="search">-------Search here------------
    <svg width="20" height="20" viewBox="0 0 20 20"><circle cx="8" cy="8" r="6" fill="none" stroke="#333" stroke-width="2.6"/><line x1="12.5" y1="12.5" x2="18" y2="18" stroke="#333" stroke-width="3"/></svg>
  </div>
</nav>
<div class="abs fold l"></div>
<div class="abs fold r"></div>

<section class="hero">
  <div class="abs slide-frame"></div>
  <div class="abs slide-inner"></div>
  <div class="ph slide-photo" role="img" aria-label="Group of pets: shepherd dog, puppy, cat, parrot, snake and mouse"></div>
  <div class="abs slide-shadow"></div>
  <h1 class="abs welcome">Welcome to Pawglint</h1>
  <h2 class="abs headline">YOUR PET SUPERSTORES</h2>
  <h3 class="abs subline">at Harrowvale and Fenwick Lake</h3>
  <ul class="abs ticks">
    <li><svg width="12" height="10"><path d="M1 5l3 3 7-7" fill="none" stroke="#1b9ad6" stroke-width="2.2"/></svg>Lorem Ipsum is simply dummy text of the printing and typesetting industry.</li>
    <li><svg width="12" height="10"><path d="M1 5l3 3 7-7" fill="none" stroke="#1b9ad6" stroke-width="2.2"/></svg>Been the industry's standard dummy text ever since the 1500s, when an unknown</li>
    <li><svg width="12" height="10"><path d="M1 5l3 3 7-7" fill="none" stroke="#1b9ad6" stroke-width="2.2"/></svg>Galley of type and scrambled it to make a type specimen book. It has survived no</li>
    <li><svg width="12" height="10"><path d="M1 5l3 3 7-7" fill="none" stroke="#1b9ad6" stroke-width="2.2"/></svg>Centuries, but also the leap into electronic typesetting,</li>
  </ul>
  <div class="abs readmore">Readmore <svg width="16" height="12"><path d="M1 1l5 5-5 5M8 1l5 5-5 5" fill="none" stroke="#e00010" stroke-width="2.4"/></svg></div>
  <div class="abs slide-arrow" style="left:112px"><svg width="16" height="28"><path d="M13 2L3 14l10 12" fill="none" stroke="#fff" stroke-width="3"/></svg></div>
  <div class="abs slide-arrow" style="left:1042px"><svg width="16" height="28"><path d="M3 2l10 12L3 26" fill="none" stroke="#fff" stroke-width="3"/></svg></div>
</section>

<section class="features">
  <div class="abs panel-wing" style="left:100px"></div>
  <div class="abs panel-wing" style="left:1063px"></div>
  <div class="abs feature-panel"></div>
  <div class="abs col-rule" style="left:438px"></div>
  <div class="abs col-rule" style="left:756px"></div>

  <h4 class="abs col-title" style="left:157px">About Comapny</h4>
  <div class="ph" style="left:158px;top:628px;width:250px;height:118px;background:linear-gradient(90deg,#4a3a2a,#c88a3a 45%,#efe2c8)" role="img" aria-label="Puppies and kittens sitting together"></div>
  <p class="abs col-text" style="left:157px;top:766px">Bibendum a, adipiscing vitae, commodo et, dui. Ut tincidunt tortor.</p>

  <h4 class="abs col-title" style="left:468px">What We Do</h4>
  <div class="ph" style="left:510px;top:640px;width:152px;height:100px;background:linear-gradient(90deg,#f2ede4,#c8302a 60%,#e8d8c0)" role="img" aria-label="Puppy in a festive hat beside gift boxes"></div>
  <p class="abs col-text" style="left:468px;top:767px">Etiam vitae nisl. In dignissim lacus ut ante. Cras elit lectus, bibendum a,</p>

  <h4 class="abs col-title" style="left:783px">Feature Product</h4>
  <div class="ph" style="left:790px;top:636px;width:234px;height:142px;background:linear-gradient(90deg,#d98a3a,#8a7a6a 45%,#e2b070)" role="img" aria-label="Kittens and a dog with pet food bowls"></div>
  <svg class="abs pager" width="30" height="14"><path d="M9 2L3 7l6 5" fill="none" stroke="#333" stroke-width="2.6"/><path d="M20 2l6 5-6 5" fill="none" stroke="#e00010" stroke-width="2.6"/></svg>
</section>

<section class="portfolio">
  <div class="ph port-icon" role="img" aria-label="Clownfish emblem"></div>
  <h4 class="abs port-title">Pet Portfolio</h4>
  <div class="abs port-rule"></div>
  <svg class="abs" style="left:145px;top:936px" width="28" height="56"><path d="M26 2L2 28l24 26" fill="#e4e4e4" stroke="#bbb" stroke-width="1.5"/></svg>
  <svg class="abs" style="left:1037px;top:936px" width="28" height="56"><path d="M2 2l24 26L2 54" fill="#e4e4e4" stroke="#bbb" stroke-width="1.5"/></svg>
  <div class="ph thumb" style="left:190px;top:916px;width:144px;height:94px;background:radial-gradient(#d8b88a,#f2f2f2 70%);border:2px solid #fff" role="img" aria-label="Two golden puppies"></div>
  <div class="ph thumb" style="left:372px;top:919px;width:139px;height:90px;background:linear-gradient(120deg,#2c7a2c,#3ed13e 45%,#1a5a1a)" role="img" aria-label="Green parrot"></div>
  <div class="ph thumb" style="left:553px;top:918px;width:131px;height:90px;background:linear-gradient(#6a8a3a,#8aa55a 50%,#5a7a2a)" role="img" aria-label="Rabbit on grass"></div>
  <div class="ph thumb" style="left:721px;top:918px;width:128px;height:90px;background:linear-gradient(120deg,#3a3a5a,#e8a868 50%,#6a6a2a)" role="img" aria-label="Cat resting on a cushion"></div>
  <div class="ph thumb" style="left:887px;top:918px;width:132px;height:90px;background:linear-gradient(#1e3a2a,#4a8a3a 50%,#2a4a3a)" role="img" aria-label="Planted aquarium"></div>
</section>

<footer>
  <div class="abs foot-rule"></div>
  <div class="abs foot-links"><span>Home</span><span>|</span><span>About Us</span><span>|</span><span>Health</span><span>|</span><span>Body</span><span>|</span><span>Skin</span><span>|</span><span>Beauty</span><span>|</span><span>Contact Us</span></div>
  <div class="abs copy">Lumavale © Copyright 2011.&nbsp;&nbsp; Privacy Policy&nbsp; |&nbsp; Terms of Use</div>
  <address class="abs address" style="font-style:normal">Shop 4 / 220 Corella Rd<br>HARROWVALE W.A 6190<br>Phone: (08) 9471 3362,&nbsp; Fax: (08) 9471 3360</address>
</footer>

</body>
</html>
```